Math Word Problems Make Your Palms Sweat??

I need a landing page for lead magnet download and email capture. Prospects will get here from QL ad. Landing page should be clean, simple and aimed at parents of Algebra 1 students. I will attach logo. Please use logo brand colors and fonts. The final design should be clear, easy to understand with struggling students and parents that don't know how to help. Copy should include: (lead magnet download info:) Number Story Rescue Pack with examples AND solutions, Conquer word problems with a step by step guide written by former teacher and full time math tutor.

Target Market(s)

Parents of struggling high school math/Algebra 1 students

Colors
33b8a4
ffffff

Requirements
Must have
• address pain points of:
struggling students
word problems causing angst
parents not knowing how to help their child

be clean, simple and easy to see what my message is via copy, images and feel of page

brand colors (ffffff, 5f5e60, 00a99d)and fonts (questrial, glacial indifference and arimo) from attached logo

clear call to action (download the pdf/lead magnet)
Nice to have
• bulleted points, not too wordy but clear message

related images/teens/struggling with math

my headshot if it looks appropriate on page

(I will likely have revisions once I see the first draft)
Should not have
• crowded
hard to read
message hard to decipher
busy
unclear call to action

```html
<!DOCTYPE html>
<html lang="en">
<head>
<meta charset="utf-8">
<title>Clearpath Tutoring – Landing Page Options</title>
<link rel="stylesheet" href="https://fonts.googleapis.com/css2?family=Poppins:wght@400;500&family=Roboto:wght@400;500&display=swap">
<style>
  :root {
    --board: #d3d3d3;
    --teal: #1fa697;
    --teal-bright: #2eb3a2;
    --slate: #555457;
    --white: #ffffff;
    --field: #f2f2f2;
    --ink: #222222;
    --muted: #555555;
  }
  * { box-sizing: border-box; margin: 0; padding: 0; }
  html, body { width: 1084px; height: 1200px; overflow: hidden; }
  body { background: var(--board); font-family: "Poppins", sans-serif; position: relative; }

  .panel { position: absolute; left: 80px; width: 924px; height: 502px; overflow: hidden; }
  .panel--dark { top: 70px; }
  .panel--teal { top: 628px; }

  .panel__backdrop { position: absolute; inset: 0; }
  .panel--dark .panel__backdrop {
    background: linear-gradient(90deg, #4b4a49 0%, #3d3a36 30%, #24302f 55%, #1b2a2a 100%);
  }
  .panel--dark .panel__backdrop::after {
    content: ""; position: absolute; left: 110px; top: 120px; width: 200px; height: 382px;
    background: radial-gradient(ellipse at 50% 70%, rgba(150,120,40,0.55), rgba(150,120,40,0) 70%);
  }
  .panel--teal .panel__backdrop {
    background: linear-gradient(90deg, #26a393 0%, #2aa898 60%, #3bb5a3 85%, #35b09f 100%);
  }
  .panel--teal .panel__backdrop::after {
    content: ""; position: absolute; right: 20px; top: 60px; width: 300px; height: 442px;
    background: radial-gradient(ellipse at 50% 45%, rgba(120,210,190,0.35), rgba(120,210,190,0) 70%);
  }

  .brand {
    position: absolute; left: 0; right: 0; top: 44px;
    display: flex; justify-content: center; align-items: center; gap: 8px;
    color: var(--white); font-size: 22px; font-weight: 500; letter-spacing: 0.2px;
  }
  .brand__mark { width: 14px; height: 14px; background: var(--teal-bright); }
  .panel--teal .brand__mark { background: var(--slate); }

  .benefits { position: absolute; left: 252px; top: 116px; list-style: none; color: var(--white); font-size: 14px; line-height: 19.5px; }
  .benefits li { position: relative; padding-left: 19px; margin-bottom: 11px; }
  .benefits svg { position: absolute; left: 0; top: 4px; width: 11px; height: 11px; }

  .cta-top {
    position: absolute; left: 389px; top: 212px; width: 147px; height: 36px;
    background: var(--white); color: var(--teal); display: flex; align-items: center; justify-content: center;
    font-family: "Roboto", sans-serif; font-weight: 500; font-size: 12px; letter-spacing: 0.2px;
  }

  .signup { position: absolute; left: 0; top: 0; width: 924px; height: 502px; }
  .signup__frame { position: absolute; left: 0; top: 0; }
  .signup__card { position: absolute; left: 265px; top: 290px; width: 393px; height: 150px; background: var(--white); }
  .signup__photo { position: absolute; left: 0; top: 0; width: 137px; height: 150px;
    background: linear-gradient(160deg, #e8e4dc 0%, #c9bfb2 45%, #8b7464 70%, #e9e6e1 100%); }
  .signup__title { position: absolute; left: 147px; top: 15px; font-size: 12.5px; font-weight: 500; color: var(--muted); }
  .signup__label { position: absolute; left: 147px; font-family: "Roboto", sans-serif; font-size: 10.5px; color: var(--ink); }
  .signup__field { position: absolute; left: 186px; width: 198px; height: 29px; background: var(--field);
    display: flex; align-items: center; gap: 5px; padding-left: 11px;
    font-family: "Roboto", sans-serif; font-size: 7.5px; color: #555; }
  .signup__field svg { width: 8px; height: 8px; }

  .download { position: absolute; left: 501px; top: 424px; width: 143px; height: 38px;
    background: var(--teal); color: var(--white); display: flex; align-items: center; justify-content: center;
    font-family: "Roboto", sans-serif; font-weight: 500; font-size: 12px; }
  .panel--teal .download { background: var(--slate); }
</style>
</head>
<body>

<section class="panel panel--dark">
  <div class="panel__backdrop" role="img" aria-label="Photo of a smiling teen girl writing math on a dark chalkboard"></div>
  <div class="brand"><span class="brand__mark"></span>Clearpath Tutoring</div>
  <ul class="benefits">
    <li><svg viewBox="0 0 12 12"><circle cx="6" cy="6" r="6" fill="#fff"/><path d="M3.3 6.2l1.8 1.8 3.6-3.6" stroke="#2a2a2a" stroke-width="1.6" fill="none"/></svg>Number Story Rescue Pack with examples AND solutions,</li>
    <li><svg viewBox="0 0 12 12"><circle cx="6" cy="6" r="6" fill="#fff"/><path d="M3.3 6.2l1.8 1.8 3.6-3.6" stroke="#2a2a2a" stroke-width="1.6" fill="none"/></svg>Conquer word problems with a step by step guide written<br>by former teacher and full time math tutor.</li>
  </ul>
  <div class="cta-top">GET YOUR PROSPECTS</div>
  <div class="signup">
    <svg class="signup__frame" width="924" height="502" viewBox="0 0 924 502">
      <polyline points="397,444 260,444 260,285 663,285 663,418" fill="none" stroke="#1fa697" stroke-width="9"/>
      <polyline points="527,470 497,470 497,419 648,419 648,432" fill="none" stroke="#1fa697" stroke-width="2.5"/>
    </svg>
    <div class="signup__card">
      <div class="signup__photo" role="img" aria-label="Headshot of the tutor"></div>
      <div class="signup__title">Download the Rescue Pack</div>
      <div class="signup__label" style="top:53px">Name:</div>
      <div class="signup__field" style="top:49px"><svg viewBox="0 0 10 10"><path d="M1 2h5M1 2v7h7V5M4 6l5-5" stroke="#555" stroke-width="1.2" fill="none"/></svg>Enter Your Name</div>
      <div class="signup__label" style="top:93px">Email:</div>
      <div class="signup__field" style="top:88px"><svg viewBox="0 0 10 10"><rect x="0.5" y="2" width="9" height="6" fill="#555"/><path d="M0.5 2l4.5 3.5L9.5 2" stroke="#fff" stroke-width="0.8" fill="none"/></svg>Enter Email Address</div>
    </div>
    <div class="download">DOWNLOAD THE PDF</div>
  </div>
</section>

<section class="panel panel--teal">
  <div class="panel__backdrop" role="img" aria-label="Teal-tinted photo of a smiling teen boy giving a thumbs up in front of a chalkboard of equations"></div>
  <div class="brand"><span class="brand__mark"></span>Clearpath Tutoring</div>
  <ul class="benefits">
    <li><svg viewBox="0 0 12 12"><circle cx="6" cy="6" r="6" fill="#fff"/><path d="M3.3 6.2l1.8 1.8 3.6-3.6" stroke="#2aa898" stroke-width="1.6" fill="none"/></svg>Number Story Rescue Pack with examples AND solutions,</li>
    <li><svg viewBox="0 0 12 12"><circle cx="6" cy="6" r="6" fill="#fff"/><path d="M3.3 6.2l1.8 1.8 3.6-3.6" stroke="#2aa898" stroke-width="1.6" fill="none"/></svg>Conquer word problems with a step by step guide written<br>by former teacher and full time math tutor.</li>
  </ul>
  <div class="cta-top">GET YOUR PROSPECTS</div>
  <div class="signup">
    <svg class="signup__frame" width="924" height="502" viewBox="0 0 924 502">
      <polyline points="397,444 260,444 260,285 663,285 663,418" fill="none" stroke="#555457" stroke-width="9"/>
      <polyline points="527,470 497,470 497,419 648,419 648,432" fill="none" stroke="#555457" stroke-width="2.5"/>
    </svg>
    <div class="signup__card">
      <div class="signup__photo" role="img" aria-label="Headshot of the tutor"></div>
      <div class="signup__title">Download the Rescue Pack</div>
      <div class="signup__label" style="top:53px">Name:</div>
      <div class="signup__field" style="top:49px"><svg viewBox="0 0 10 10"><path d="M1 2h5M1 2v7h7V5M4 6l5-5" stroke="#555" stroke-width="1.2" fill="none"/></svg>Enter Your Name</div>
      <div class="signup__label" style="top:93px">Email:</div>
      <div class="signup__field" style="top:88px"><svg viewBox="0 0 10 10"><rect x="0.5" y="2" width="9" height="6" fill="#555"/><path d="M0.5 2l4.5 3.5L9.5 2" stroke="#fff" stroke-width="0.8" fill="none"/></svg>Enter Email Address</div>
    </div>
    <div class="download">DOWNLOAD THE PDF</div>
  </div>
</section>

</body>
</html>
```